Need simple and modern looking business card with all my information on one side and logo on the other side
Info :
Company name - VELMAR CONSTRUCTION LLC
Company addres- 418 harbor 87th. Dunmoor park ny 10352
Email- velmarllc@tridomail.Com
Company phone number 555-318-6094
Cell number- 555-742-0583
Web site - velmarllc.Com
My name Gerald tomasino

Target Market(s)

Construction , home improvement, remodeling

Industry/Entity Type

Construction

Contact Information for Business Card

It has to be moder but at the same time simple

Font styles to use
Sans Serif

Colors
0255a3
ffffff
000000
f78f20
b1b1b1
9d9d9d
1b1b1b
33a6d7
ec1f27

Requirements
Must have
• My logo on one side maybe with a some kind of background on the other side all my information
Nice to have
• Some kind of background pictures provided by you .PLEASE HAVE ACCOUNT WITH PIXELVAULT WILL NOT PAY ANY EXTRA FEES .
Should not have
• Any kind of hamer, nails,screws, helmets itp. Please do not copy the other designs come up with something new.

```html
<!DOCTYPE html>
<html lang="en">
<head>
<meta charset="utf-8">
<title>Velmar Construction LLC – Business Card</title>
<link href="https://fonts.googleapis.com/css2?family=Open+Sans:wght@400;600;700&display=swap" rel="stylesheet">
<style>
  :root {
    --blue: #0255a3;
    --white: #ffffff;
    --black: #000000;
    --orange: #f78f20;
    --grey-light: #b1b1b1;
    --grey: #9d9d9d;
    --ink: #1b1b1b;
    --sky: #33a6d7;
    --red: #ec1f27;
    --stage: #ececec;
    --text: #222222;
  }
  * { box-sizing: border-box; margin: 0; padding: 0; }
  html, body { width: 1200px; height: 1000px; overflow: hidden; }
  body {
    background: var(--stage);
    font-family: "Open Sans", Arial, sans-serif;
    position: relative;
  }
  .card {
    position: absolute;
    left: 265px;
    width: 665px;
    height: 397px;
    background: var(--white);
    overflow: hidden;
  }
  .card--front { top: 73px; }
  .card--back { top: 533px; }

  /* wordmark */
  .wordmark {
    position: absolute;
    display: flex;
    align-items: center;
    gap: 12px;
    color: var(--ink);
    font-weight: 700;
  }
  .wordmark__square {
    width: 22px; height: 22px;
    background: var(--orange);
    flex: none;
  }
  .wordmark__text { line-height: 1; }
  .wordmark__name { display: block; letter-spacing: 1px; }
  .wordmark__sub { display: block; letter-spacing: 1.5px; margin-top: 6px; }

  .card--front .wordmark { right: 32px; top: 125px; }
  .card--front .wordmark__name { font-size: 54px; }
  .card--front .wordmark__sub { font-size: 17px; }

  .card--back .wordmark { left: 140px; top: 205px; }
  .card--back .wordmark__name { font-size: 60px; }
  .card--back .wordmark__sub { font-size: 19px; }

  /* holder */
  .holder { position: absolute; left: 33px; top: 170px; }
  .holder__name { color: var(--orange); font-size: 21px; font-weight: 400; line-height: 1.2; }
  .holder__title { color: var(--text); font-size: 16px; margin-top: 2px; }

  .contacts {
    position: absolute; left: 35px; top: 246px;
    list-style: none;
    font-size: 16px; color: var(--text);
  }
  .contacts li { display: flex; align-items: center; gap: 6px; height: 24px; }
  .contacts svg { width: 14px; height: 14px; fill: var(--blue); flex: none; }
  .address {
    position: absolute; left: 33px; top: 349px;
    font-size: 16px; color: var(--text);
  }

  .colour-bands {
    position: absolute; left: 0; bottom: 0; width: 100%; height: 8px;
    display: flex; gap: 4px;
  }
  .colour-bands span { flex: 1; }
  .colour-bands .band--orange { background: var(--orange); }
  .colour-bands .band--blue { background: var(--blue); }
  .colour-bands .band--red { background: var(--red); }

  .site-photo {
    position: absolute; inset: 0;
    background: linear-gradient(120deg, #dfe3e8 0%, #f3f5f8 45%, #e8ecef 70%, #d9dde0 100%);
  }
</style>
</head>
<body>

  <section class="card card--front" aria-label="Business card, contact side">
    <div class="wordmark">
      <span class="wordmark__square"></span>
      <span class="wordmark__text">
        <span class="wordmark__name">VELMAR</span>
        <span class="wordmark__sub">CONSTRUCTION LLC</span>
      </span>
    </div>

    <div class="holder">
      <p class="holder__name">Gerald tomasino</p>
      <p class="holder__title">President</p>
    </div>

    <ul class="contacts">
      <li>
        <svg viewBox="0 0 14 14" aria-hidden="true"><rect x="3.5" y="0.5" width="7" height="13" rx="1.2"/><rect x="5" y="2.5" width="4" height="6" fill="#fff"/></svg>
        555-742-0583
      </li>
      <li>
        <svg viewBox="0 0 14 14" aria-hidden="true"><path d="M1 5c0-2 3-3.5 6-3.5S13 3 13 5l-3 1V4.5H4V6zM3 7h8l1.5 5.5h-11z"/></svg>
        555-318-6094
      </li>
      <li>
        <svg viewBox="0 0 14 14" aria-hidden="true"><rect x="0.5" y="2.5" width="13" height="9"/><path d="M1 3l6 5 6-5" stroke="#fff" stroke-width="1.2" fill="none"/></svg>
        velmarllc@tridomail.com
      </li>
      <li>
        <svg viewBox="0 0 14 14" aria-hidden="true"><circle cx="7" cy="7" r="6.5"/><path d="M0.5 7h13M7 0.5c-3 3-3 10 0 13M7 0.5c3 3 3 10 0 13" stroke="#fff" stroke-width="0.9" fill="none"/></svg>
        www.velmarllc.com
      </li>
    </ul>

    <p class="address">418 Harbor 87th St, Dunmoor Park, NY 10352</p>

    <div class="colour-bands" aria-hidden="true">
      <span class="band--orange"></span>
      <span class="band--blue"></span>
      <span class="band--red"></span>
    </div>
  </section>

  <section class="card card--back" aria-label="Business card, logo side">
    <div class="site-photo" role="img" aria-label="Faded photograph of a construction site with scaffolding, cranes and a worker in a high-visibility jacket"></div>
    <div class="wordmark">
      <span class="wordmark__square"></span>
      <span class="wordmark__text">
        <span class="wordmark__name">VELMAR</span>
        <span class="wordmark__sub">CONSTRUCTION LLC</span>
      </span>
    </div>
  </section>

</body>
</html>
```